Web Design Accounting-Tax and related business service online.

We are looking to develop a website/online application for users in the South African market to register and buy Accounting/tax and related services online. (New business registrations/Income tax returns/Payroll) etc

The Domain will be www.ledgerpoint-hub.co.za and the business will be run under Velmira Financial Services.

The domain - www.ledgerpoint-hub.co.za will be used as the "trading" name of the site, so any sections that possible make use name use domain name.

We are looking for designs for the website.

Here is the requirements as from the developer

• Home Page: Design of the home page of the website.
• Forms: We have different forms in the application. Need any one form designed. Just look and feel without functionality.
• Member Area: when a user will log in, the layout of dashboard to show them.

UPDATE (Previously HTML required) - Can be in PSD format for this Contest.

(If you prepared/capable to handle the PSD to HTML conversation you can quote seperate for this)

Websites that offer similar services (Not for design inspiration please, but idea of possible website layout etc)

http://www.bramblecount-web.co.za/
http://www.quillmark-enrolments.co.za/

See our current static website for colour schemes that I like.

www.velmira.co.za

Prefer clean, modern - uncluttered look.

Target Market(s)

Users that pefer employing tech and ease of obtaining services online to having Accountant physically close.

Industry/Entity Type

Business Service

Requirements
Must have
• Clean, Modern, uncluttered look.

Nice to have

Should not have
• Old "boring" stiff accounting designs. No clutter or too busy.

```html
<!DOCTYPE html>
<html lang="en">
<head>
<meta charset="utf-8">
<title>Velmira Financial Services</title>
<link rel="stylesheet" href="https://fonts.googleapis.com/css2?family=Arvo:wght@700&family=Tinos:wght@400;700&family=Handlee&family=Open+Sans:wght@400&display=swap">
<style>
  :root {
    --green-dark: #4f8a23;
    --green-top: #6fbf3a;
    --green-light: #a6ec6c;
    --green-pale: #c9f4a2;
    --nav-hi: #b4f06a;
    --nav-lo: #52b91d;
    --grey-band: #cccccc;
    --ink: #111111;
    --ink-soft: #555555;
    --panel: #ffffff;
    --panel-line: #c8c8c8;
    --arrow: #c6f58e;
    --tag-blue: #5a8fcf;
    --header-link: #b3b3b3;
  }
  * { box-sizing: border-box; margin: 0; padding: 0; }
  html, body { width: 1200px; height: 900px; overflow: hidden; }
  body {
    position: relative;
    font-family: "Tinos", "Times New Roman", serif;
    color: var(--ink);
    background: linear-gradient(180deg, var(--green-light) 0%, var(--green-light) 60%, #9ee863 100%);
  }
  .topbar {
    position: absolute; left: 0; top: 0; width: 1200px; height: 43px;
    background: linear-gradient(90deg, var(--green-dark), #5f9e2c 50%, var(--green-dark));
  }
  .topbar a {
    position: absolute; top: 6px; font-size: 29px; color: var(--header-link);
    text-decoration: none; font-family: "Tinos", serif;
  }
  .topbar .register { left: 752px; }
  .topbar .login { left: 976px; }
  .hero-glow {
    position: absolute; left: 0; top: 43px; width: 1200px; height: 212px;
    background: radial-gradient(ellipse at 30% 20%, #e9ffd6 0%, var(--green-light) 45%, #95e058 100%);
  }
  .brand {
    position: absolute; left: 0; top: 43px; width: 372px; height: 111px; background: var(--panel);
    display: flex; align-items: center; gap: 16px; padding-left: 24px;
  }
  .brand-dot { width: 70px; height: 70px; border-radius: 50%; background: var(--nav-lo); flex: none; }
  .brand-name { font-size: 30px; color: #333; line-height: 1.1; }
  .brand-reg { font-size: 9px; color: #6a7fa8; display: block; margin-top: 4px; }
  .nav {
    position: absolute; left: 32px; top: 153px; width: 1138px; height: 72px;
    background: linear-gradient(180deg, var(--nav-hi) 0%, #7fd63a 55%, var(--nav-lo) 100%);
    border: 1px solid #e6ffd0; box-shadow: 0 8px 14px rgba(60,120,20,.35);
  }
  .nav a {
    position: absolute; top: 14px; font-family: "Arvo", serif; font-weight: 700;
    font-size: 32px; color: #fff; text-decoration: none;
  }
  .band { position: absolute; left: 0; top: 255px; width: 1200px; height: 207px; background: var(--grey-band); }
  .welcome-title { position: absolute; left: 10px; top: 259px; font-size: 18px; }
  .welcome-copy { position: absolute; left: 14px; top: 299px; width: 372px; font-size: 11.3px; line-height: 1.2; }
  .welcome-copy p + p { margin-top: 12px; }
  .showcase {
    position: absolute; left: 390px; top: 263px; width: 790px; height: 197px;
    background: #bdbdbd; border: 1px solid #aaa;
  }
  .reel {
    position: absolute; left: 0; top: 16px; width: 790px; height: 140px;
    background: linear-gradient(90deg, #6fb6d8, #2a8a96 20%, #9bc46a 45%, #c9724a 60%, #b98a5a 75%, #5ab0c2 100%);
    border-top: 12px solid #111; border-bottom: 12px solid #111;
  }
  .showcase-title {
    position: absolute; left: 718px; top: 237px; font-family: "Handlee", cursive;
    font-size: 38px; color: var(--tag-blue); letter-spacing: 1px;
  }
  .showcase-tag {
    position: absolute; left: 396px; top: 418px; font-family: "Open Sans", sans-serif;
    font-size: 32px; color: var(--tag-blue); word-spacing: 6px;
  }
  .showcase-tag .online { position: absolute; left: 602px; white-space: nowrap; }
  .services {
    position: absolute; left: 26px; top: 485px; width: 1150px; height: 399px;
    background: #f4f4f4; border: 1px solid var(--panel-line);
  }
  .section-title {
    position: absolute; top: 497px; font-size: 29px; color: var(--ink-soft);
    text-shadow: 1px 1px 2px rgba(0,0,0,.25);
  }
  .rule { position: absolute; left: 27px; top: 532px; width: 1148px; height: 1px; background: var(--panel-line); }
  .box { position: absolute; background: var(--panel); border: 1px solid var(--panel-line); }
  .box-individual { left: 33px; top: 547px; width: 690px; height: 323px; }
  .box-package { left: 740px; top: 545px; width: 426px; height: 326px; }
  .group { position: absolute; }
  .group h3 { font-weight: 400; font-size: 22px; margin-bottom: 10px; }
  .group li { list-style: none; font-size: 13.5px; line-height: 16.6px; }
  .software { position: absolute; left: 39px; top: 686px; }
  .software b {
    display: block; font-weight: 400; font-size: 21px;
    background: linear-gradient(90deg, #2a7cd6, #4cc43a); -webkit-background-clip: text; background-clip: text; color: transparent;
  }
  .software span { display: block; font-size: 13px; color: #3a9a3a; margin-left: 2px; }
  .package { position: absolute; left: 768px; display: flex; gap: 10px; font-size: 25px; line-height: 30px; }
  .package svg { flex: none; margin-top: 2px; }
</style>
</head>
<body>
  <header class="topbar">
    <a class="register" href="#">Register</a>
    <a class="login" href="#">Log In</a>
  </header>
  <div class="hero-glow"></div>
  <div class="brand">
    <div class="brand-dot"></div>
    <div class="brand-name">Velmira<br><span style="font-size:16px">Financial Services CC</span><span class="brand-reg">CK 2009/104418/23</span></div>
  </div>
  <nav class="nav">
    <a href="#" style="left:44px">Home</a>
    <a href="#" style="left:264px">Services</a>
    <a href="#" style="left:512px">Client feedback</a>
    <a href="#" style="left:884px">Contact us</a>
  </nav>

  <section class="band"></section>
  <h1 class="welcome-title" style="font-weight:400">Welcome to Velmira Financial Services</h1>
  <div class="welcome-copy">
    <p>Velmira is a word we chose meaning "to prosper".</p>
    <p>We believe in providing you with all the financial services,<br>tools and support you need to move from surviving (or not)<br>to prosper at competitive rates!<br>We specialize in providing solutions for startup companies to medium enterprises to help you comply with all statutory requirements as well as provide you with the means to measure performance and make the right choice based on these figures. So contact us today for a FREE assessment of your requirements and we will tailor a solution to your budget!</p>
  </div>
  <div class="showcase">
    <div class="reel" role="img" aria-label="Film strip of travel scenes: beaches, canals, coastlines, blossoms and old towns"></div>
  </div>
  <div class="showcase-title">START THE LIFE</div>
  <div class="showcase-tag">Accounting...we can take it on<span class="online">ON line</span></div>

  <section class="services"></section>
  <h2 class="section-title" style="left:38px;font-weight:400">Individual services</h2>
  <h2 class="section-title" style="left:744px;font-weight:400">Package services</h2>
  <div class="rule"></div>
  <div class="box box-individual"></div>
  <div class="box box-package"></div>

  <div class="group" style="left:39px;top:554px">
    <h3>Business Registration services</h3>
    <ul>
      <li>Register a Close Corporation</li>
      <li>Register for Income Tax</li>
      <li>Register for PAYE/UIF/SDL</li>
      <li>Register for VAT</li>
      <li>Register WCF</li>
    </ul>
  </div>
  <div class="software"><b>Ledgerline Software</b><span>Sales &amp; Support</span></div>
  <div class="group" style="left:39px;top:754px">
    <h3>Individual Services</h3>
    <ul>
      <li>Register for income tax</li>
      <li>Income Tax returns</li>
      <li>Tax Clearance certificate</li>
    </ul>
  </div>
  <div class="group" style="left:384px;top:554px">
    <h3>Business services</h3>
    <ul>
      <li>Bookeeping/Accounting Solutions</li>
      <li>Income tax return</li>
      <li>Full Payroll function</li>
      <li>VAT Returns</li>
      <li>IRP5 Certificates</li>
      <li>Annual Financial Statements</li>
      <li>Management Accounts</li>
      <li>CIPRO Returns</li>
      <li>WCF Returns</li>
      <li>Tax Clearance Certificate</li>
      <li>Business Consulting Services</li>
    </ul>
  </div>
  <div class="group" style="left:383px;top:791px">
    <h3>Domestic workers</h3>
    <ul>
      <li>UIF Registrations</li>
      <li>UIF Payments</li>
    </ul>
  </div>

  <div class="package" style="top:592px">
    <svg width="28" height="30" viewBox="0 0 28 30"><path d="M2 0 L28 15 L2 30 L10 15 Z" fill="var(--arrow)"/></svg>
    <span>Start a business package</span>
  </div>
  <div class="package" style="top:682px">
    <svg width="28" height="30" viewBox="0 0 28 30"><path d="M2 0 L28 15 L2 30 L10 15 Z" fill="var(--arrow)"/></svg>
    <span>Bookkeeping/Accounting/<br>Payroll/Tax package</span>
  </div>
  <div class="package" style="top:778px">
    <svg width="28" height="30" viewBox="0 0 28 30"><path d="M2 0 L28 15 L2 30 L10 15 Z" fill="var(--arrow)"/></svg>
    <span>Domestic workers UIF</span>
  </div>
</body>
</html>
```